Redesign Of Flower Delivery Subscription Service Website

I need a revamped website of www.petal-rush.com

Please revamp current design using same content....

Target Market(s)

people who buy flowers. Brides, wedding planners, wedding photographer, married man, boyfriend, etc.

Industry/Entity Type

Florist

Number of Pages Required

5+ page

Colors

Designer to choose colors to be used in the design.

Requirements
Must have
• I need a revamped website of www.petal-rush.com
• Please revamp current design using same content....
Nice to have
Should not have

```html
<!DOCTYPE html>
<html lang="en">
<head>
<meta charset="utf-8">
<title>PetalRush – Monthly Flower Delivery</title>
<link rel="stylesheet" href="https://fonts.googleapis.com/css2?family=Great+Vibes&family=Courgette&family=Open+Sans:ital,wght@0,400;0,600;0,700;1,400&display=swap">
<style>
:root{
  --sky:#3a8fd8;
  --sky-deep:#2a86dc;
  --cart:#3d9be9;
  --white:#ffffff;
  --pink-band:#ee8eb0;
  --pink-band-dark:#e27aa0;
  --pink-text:#c05c85;
  --gold:#dcb563;
  --gold-dark:#c99a45;
  --orange:#cf5f18;
  --magenta:#de62cc;
  --magenta-dark:#c449b6;
  --plum:#9c1f96;
  --ink:#3b2a35;
  --leaf:#2f6a2a;
  --leaf-light:#6fae55;
}
*{box-sizing:border-box;margin:0;padding:0}
html,body{width:1200px;height:2507px;overflow:hidden}
body{position:relative;font-family:"Open Sans",sans-serif;color:var(--ink);background:var(--white)}

/* Hero */
.hero{position:absolute;left:0;top:0;width:1200px;height:618px;
  background:linear-gradient(180deg,#dcecf7 0%,#c9e2ef 35%,#a9cbb3 70%,#9dbf98 100%)}
.brand{position:absolute;left:37px;top:40px;display:flex;align-items:center;gap:12px;
  font-weight:700;font-size:36px;color:var(--sky-deep)}
.brand-dot{width:22px;height:22px;border-radius:50%;background:var(--sky-deep)}
.nav a{position:absolute;font-size:18px;color:var(--sky);text-decoration:none;white-space:nowrap}
.cart{position:absolute;left:1065px;top:18px;width:105px;height:96px;background:var(--cart);
  border:3px solid var(--white);border-radius:8px;display:flex;align-items:center;justify-content:center}
.hanging-basket{position:absolute;left:37px;top:138px;width:535px;height:397px;border-radius:45% 45% 50% 50%;
  background:radial-gradient(ellipse at 50% 45%,#f4a9bf 0%,#ee6f95 40%,#9fc78c 75%,rgba(160,200,150,0) 100%)}
.hero-title{position:absolute;left:560px;top:168px;width:586px;text-align:center;
  font-family:"Great Vibes",cursive;font-weight:400;font-size:96px;line-height:1;color:var(--sky-deep)}
.hero-sub{position:absolute;left:560px;width:586px;text-align:center;font-style:italic;font-size:19px;color:#3b9be8}
.perk-icon{position:absolute;top:397px;width:80px;height:107px;background:rgba(255,255,255,.85);border-radius:40% 40% 20% 20%}
.perk{position:absolute;top:513px;height:41px;border:3px solid var(--white);border-radius:9px;
  background:rgba(255,255,255,.22);color:var(--white);font-size:18px;display:flex;align-items:center;justify-content:center}

/* Email band */
.email-band{position:absolute;left:0;top:618px;width:1200px;height:262px;
  background:repeating-linear-gradient(180deg,var(--pink-band) 0 64px,var(--pink-band-dark) 64px 66px)}
.email-panel{position:absolute;left:236px;top:47px;width:724px;height:169px;border-radius:10px;background:rgba(255,255,255,.16)}
.email-lead{position:absolute;left:0;top:24px;width:100%;text-align:center;font-style:italic;color:var(--white);font-size:18px}
.email-field{position:absolute;left:28px;top:72px;width:668px;height:72px;border:3px solid var(--white);border-radius:12px;
  background:rgba(255,255,255,.18);display:flex;align-items:center;justify-content:center;color:var(--pink-text);font-size:16px}
.arrow{position:absolute;top:136px}

/* Features */
.features{position:absolute;left:0;top:880px;width:1200px;height:612px;
  background:radial-gradient(circle at 20% 30%,#e9c877 0,rgba(0,0,0,0) 35%),radial-gradient(circle at 85% 70%,#e7c46f 0,rgba(0,0,0,0) 40%),linear-gradient(180deg,var(--gold),var(--gold-dark))}
.photo{position:absolute;top:47px;height:339px;border:4px solid var(--white);border-radius:12px}
.feature-card{position:absolute;top:434px;height:131px;border:3px solid var(--white);border-radius:9px;
  background:rgba(255,241,205,.6);text-align:center;padding:8px 12px 0;overflow:hidden}
.feature-card h3{font-family:"Courgette",cursive;font-weight:400;font-size:22px;line-height:30px;color:var(--orange);white-space:nowrap}
.feature-card p{font-size:14.5px;line-height:23px;height:46px;overflow:hidden}
.feature-card .read-more{display:block;font-family:"Courgette",cursive;font-size:18px;line-height:24px;color:var(--orange)}

/* About */
.about{position:absolute;left:0;top:1492px;width:1200px;height:797px;
  background:repeating-linear-gradient(180deg,var(--magenta) 0 88px,var(--magenta-dark) 88px 90px)}
.about-title{position:absolute;left:270px;top:42px;width:712px;text-align:center;font-family:"Courgette",cursive;font-weight:400;
  font-size:24px;line-height:1.3;color:var(--white)}
.about-intro{position:absolute;left:270px;top:119px;width:712px;height:104px;border:2px solid var(--white);border-radius:6px;
  background:rgba(255,255,255,.6);padding:10px 16px;font-size:13px;line-height:20px;text-align:center;overflow:hidden}
.about-intro span{display:-webkit-box;-webkit-box-orient:vertical;-webkit-line-clamp:4;overflow:hidden}
.rose{position:absolute;top:248px;width:70px;height:78px;border-radius:50% 50% 40% 40%;background:rgba(255,255,255,.9)}
.about-card{position:absolute;top:336px;width:301px;height:409px;border:3px solid var(--white);border-radius:10px;
  background:rgba(255,255,255,.6);text-align:center;padding:12px 16px 10px;display:flex;flex-direction:column;overflow:hidden}
.about-card h3,.center-heading{font-family:"Courgette",cursive;font-weight:400;font-size:24px;line-height:34px;color:var(--plum)}
.about-card p{font-size:14px;line-height:21px;margin-top:8px;display:-webkit-box;-webkit-box-orient:vertical;overflow:hidden}
.about-card .read-more{margin-top:auto;font-family:"Courgette",cursive;font-size:22px;line-height:30px;color:var(--plum)}
.center-heading{position:absolute;left:430px;top:345px;width:340px;text-align:center;color:var(--white)}
.center-box{position:absolute;left:452px;top:493px;width:296px;height:210px;border:2px solid var(--white);border-radius:8px;
  background:rgba(255,255,255,.65);padding:9px 12px;font-size:14px;line-height:21px;text-align:center;overflow:hidden}
.center-box span{display:-webkit-box;-webkit-box-orient:vertical;-webkit-line-clamp:9;overflow:hidden}
.center-more{position:absolute;left:452px;top:720px;width:296px;text-align:center;font-family:"Courgette",cursive;font-size:22px;color:var(--plum)}

/* Footer */
.footer{position:absolute;left:0;top:2289px;width:1200px;height:218px;
  background:linear-gradient(90deg,var(--leaf) 0%,var(--leaf-light) 45%,#3f7a35 75%,#2c5f26 100%);color:var(--white)}
.footer-brand{position:absolute;left:26px;top:40px;display:flex;align-items:center;gap:10px;font-weight:700;font-size:32px;color:var(--white)}
.footer-brand span{width:18px;height:18px;border-radius:50%;background:var(--white)}
.copyright{position:absolute;left:26px;top:134px;font-size:14px;font-weight:700;line-height:1.6}
.legal{position:absolute;left:26px;top:188px;font-size:13px}
.footer h4{position:absolute;font-family:"Courgette",cursive;font-weight:400;font-size:22px}
.contact{position:absolute;left:369px;font-size:13px;display:flex;gap:10px;align-items:flex-start;line-height:1.3}
.services{position:absolute;left:689px;top:108px;list-style:none;font-size:13px;line-height:28px}
.tulips{position:absolute;left:886px;top:0;width:314px;height:218px;
  background:radial-gradient(ellipse at 50% 40%,#e8876a 0%,#c96a4c 35%,rgba(60,110,50,0) 75%)}
</style>
</head>
<body>

<header class="hero" role="img" aria-label="Soft blurred sky and green hillside background">
  <div class="brand"><span class="brand-dot"></span>PetalRush</div>
  <nav class="nav">
    <a style="left:286px;top:28px">Home</a>
    <a style="left:388px;top:28px">How it Works</a>
    <a style="left:545px;top:28px">Free Flowers Monthly</a>
    <a style="left:775px;top:28px">Delivery Areas</a>
    <a style="left:941px;top:28px">Help</a>
    <a style="left:323px;top:76px">Franchise</a>
    <a style="left:441px;top:76px">Corporate Arrangements</a>
    <a style="left:709px;top:76px">My Account</a>
    <a style="left:864px;top:76px">Blogs</a>
  </nav>
  <a class="cart" aria-label="Cart">
    <svg width="54" height="48" viewBox="0 0 54 48" fill="none" stroke="#fff" stroke-width="4" stroke-linejoin="round" stroke-linecap="round">
      <path d="M3 5h8l6 26h28l5-18H14"/><circle cx="21" cy="41" r="3.5" fill="#fff"/><circle cx="41" cy="41" r="3.5" fill="#fff"/>
    </svg>
  </a>
  <div class="hanging-basket" role="img" aria-label="Hanging basket of pink petunias"></div>
  <h1 class="hero-title">Always Fresh</h1>
  <p class="hero-sub" style="top:290px">Beautiful Flower Arrangements Delivered Monthly</p>
  <p class="hero-sub" style="top:330px">Now only $69.95/MTH ($100 value)</p>
  <div class="perk-icon" role="img" aria-label="Vase icon" style="left:552px;width:60px"></div>
  <div class="perk-icon" role="img" aria-label="Bouquet icon" style="left:770px"></div>
  <div class="perk-icon" role="img" aria-label="Gift box icon" style="left:1024px;width:92px;border-radius:8px"></div>
  <div class="perk" style="left:487px;width:190px">Free Vase</div>
  <div class="perk" style="left:703px;width:214px">Free Delivery</div>
  <div class="perk" style="left:973px;width:192px">Free Upgrade</div>
</header>

<section class="email-band">
  <svg class="arrow" style="left:30px" width="26" height="36" viewBox="0 0 26 36"><path d="M22 3 4 18l18 15Z" fill="none" stroke="#fff" stroke-width="3" stroke-linejoin="round"/></svg>
  <div class="email-panel">
    <p class="email-lead">Enter Your Email To Receive A FREE UPGRADE</p>
    <div class="email-field">Email Address</div>
  </div>
  <svg class="arrow" style="left:1146px" width="26" height="36" viewBox="0 0 26 36"><path d="M4 3l18 15L4 33Z" fill="none" stroke="#fff" stroke-width="3" stroke-linejoin="round"/></svg>
</section>

<section class="features" role="img" aria-label="Background of soft yellow chrysanthemums">
  <div class="photo" role="img" aria-label="Peach roses with greenery in a red vase" style="left:65px;width:291px;background:linear-gradient(160deg,#f7f4f0,#e8a08a 55%,#6d8a4c)"></div>
  <div class="photo" role="img" aria-label="Cream roses with purple accents in a glass vase" style="left:452px;width:288px;background:linear-gradient(160deg,#f0e7cf,#efd9c7 50%,#b98c93)"></div>
  <div class="photo" role="img" aria-label="Purple and lavender flowers in a vase with a ribbon" style="left:842px;width:286px;background:linear-gradient(160deg,#e1e6d6,#8c4f86 50%,#b7a0c8)"></div>

  <div class="feature-card" style="left:50px;width:325px">
    <h3>Set It And Forget It</h3>
    <p>PetalRush is a “SET IT and FORGET IT” subscription based flower delivery</p>
    <span class="read-more">Read More</span>
  </div>
  <div class="feature-card" style="left:436px;width:325px">
    <h3>But Never Forget Again</h3>
    <p>When setting up your account, you can choose exact delivery dates for the</p>
    <span class="read-more">Read More</span>
  </div>
  <div class="feature-card" style="left:823px;width:323px">
    <h3>Making Someone’s Day Better</h3>
    <p>Be the hero in that special someone’s life each and every month. It feels good</p>
    <span class="read-more">Read More</span>
  </div>
</section>

<section class="about" role="img" aria-label="Pink wooden boards with baby's breath sprigs">
  <h2 class="about-title">Monthly Subscription Based Flower Delivery Service in San Diego – CA by Our Florist Shop</h2>
  <p class="about-intro"><span>Every moment of life could be cherished perfectly.......IF you choose wisely. To make your day more treasured, remember that flowers are the smartest choice when delivered through our monthly PetalRush subscription based delivery service. Our online subscription-based flower delivery service can help you pamper, cherish and make an everlasting impression on the minds of your loved ones with a doorstep</span></p>

  <div class="rose" role="img" aria-label="Rose emblem" style="left:161px"></div>
  <div class="rose" role="img" aria-label="Rose emblem" style="left:561px"></div>
  <div class="rose" role="img" aria-label="Rose emblem" style="left:973px"></div>

  <article class="about-card" style="left:37px">
    <h3>Exotic Flowers Garnished With Special Hues To Compliment Your Loved Ones</h3>
    <p style="-webkit-line-clamp:9">Let’s not forget a single day in which you can make your loved ones feel special. Whether it’s your anniversary or a birthday in your family, you must always go an extra mile to show “how much I care about you.” Nothing can compare to your show of love, or compliment the joy of your loved ones, more than a perfectly blossomed bouquet of flowers. So if you</p>
    <span class="read-more">Read More</span>
  </article>

  <h3 class="center-heading">Standard And Personalized Flower Arrangements For Special Occasions</h3>
  <p class="center-box"><span>PetalRush offers on time subscription based service that is risk free, trouble free and affordable at the same time. We offer the most trusted and delightful flower delivery service in San Diego, and are designed to deliver your desired floral arrangements within your requested days and times. Our local florists will happily take your orders online for your</span></p>
  <span class="center-more">Read More</span>

  <article class="about-card" style="left:862px;width:299px">
    <h3>Get Yourself Subscribed And Claim Discounts On Big Orders!</h3>
    <p style="-webkit-line-clamp:10">Get love and adulation by gifting flowers to your loved ones on those special occasions. Whether it’s formal, personal or your love for your family, just follow the subscription criteria and get your hands on the most valuable service for all kinds of events, occasions and parties. Set up your account and select the right delivery dates for the special months and leave the rest to us. We will deliver your flowers on the exact</p>
    <span class="read-more">Read More</span>
  </article>
</section>

<footer class="footer" role="img" aria-label="Blurred green garden background">
  <div class="footer-brand"><span></span>PetalRush</div>
  <p class="copyright">Copyright © 2018.<br>All Rights Reserved.</p>
  <p class="legal">Privacy Policy Terms &amp; Conditions</p>

  <h4 style="left:447px;top:64px">Contact Info</h4>
  <div class="contact" style="top:116px">
    <svg width="14" height="18" viewBox="0 0 14 18"><path d="M7 1a6 6 0 0 0-6 6c0 4.5 6 10 6 10s6-5.5 6-10a6 6 0 0 0-6-6Z" fill="#fff"/><circle cx="7" cy="7" r="2.2" fill="#4d8a3e"/></svg>
    <span>418 Harbor Crest Way,<br>Bayview CA 92000</span>
  </div>
  <div class="contact" style="top:160px">
    <svg width="16" height="12" viewBox="0 0 16 12"><rect x="0" y="0" width="16" height="12" rx="1.5" fill="#fff"/><path d="M1 1l7 6 7-6" fill="none" stroke="#4d8a3e" stroke-width="1.5"/></svg>
    <span>Email: support@petalrush-sd.com</span>
  </div>
  <div class="contact" style="top:187px">
    <svg width="15" height="15" viewBox="0 0 15 15"><path d="M3 1l3 3-1.6 2a8 8 0 0 0 4.6 4.6l2-1.6 3 3-2 2C6 13.5 1.5 9 1 3Z" fill="#fff"/></svg>
    <span>555-204-7718</span>
  </div>

  <h4 style="left:701px;top:64px">More Services</h4>
  <ul class="services">
    <li>Corporate Arrangements</li>
    <li>Hotel Arrangements</li>
    <li>Events</li>
    <li>Weddings</li>
  </ul>
  <div class="tulips" role="img" aria-label="Peach tulips"></div>
</footer>

</body>
</html>
```